依頼詳細
館銘板、シンプルでカッコいいものを希望しております。
目線の高さに取付する予定です。
背景が黒なので、映えるものがいいです。
記載項目
3階建てアパートの1階 道路面に面したところに、館銘板位置を想定しております。大きさは、タテ300㎜xヨコ300㎜にて考えております。
日当たりのよいところです。
希望イメージ
シンプル 複雑
単色 カラフル
暗い 明るい
日常 高級
遊び心 厳粛
未来的 伝統的
女性的 男性的
希望する色
納品ファイル
• 高解像度JPG (.jpg)
補足説明

アパートの部屋がちょうど3室あり、他のデザインより目を引いたから

多くのご提案をしていただきありがとうございます。

```html
<!DOCTYPE html>
<html lang="ja">
<head>
<meta charset="utf-8">
<title>MAISON 316 館銘板</title>
<link rel="stylesheet" href="https://fonts.googleapis.com/css2?family=Noto+Serif:wght@700&display=swap">
<style>
  :root {
    --wall: #3b403e;
    --plate-light: #e4e4e3;
    --plate-mid: #cdcdcc;
    --plate-dark: #b9b9b8;
    --ink: #353837;
  }
  * { margin: 0; padding: 0; box-sizing: border-box; }
  html, body {
    width: 846px;
    height: 1200px;
    overflow: hidden;
    background: var(--wall);
  }
  .canvas {
    position: relative;
    width: 846px;
    height: 1200px;
  }
  .nameplate {
    position: absolute;
    left: 160px;
    top: 350px;
    width: 526px;
    height: 536px;
    box-shadow: 0 6px 14px rgba(0, 0, 0, 0.35);
  }
  .nameplate__surface {
    position: absolute;
    inset: 0;
    width: 100%;
    height: 100%;
  }
  .nameplate__text {
    position: absolute;
    inset: 0;
    display: flex;
    flex-direction: column;
    align-items: center;
    justify-content: center;
    color: var(--ink);
    font-family: "Noto Serif", Georgia, serif;
    font-weight: 700;
    text-align: center;
  }
  .nameplate__name {
    font-size: 84px;
    line-height: 1;
    letter-spacing: 1px;
    margin-top: -14px;
  }
  .nameplate__number {
    font-size: 150px;
    line-height: 1;
    margin-top: 4px;
  }
</style>
</head>
<body>
  <main class="canvas">
    <section class="nameplate">
      <svg class="nameplate__surface" viewBox="0 0 526 536" role="img" aria-label="Brushed silver plate with a white interlocking circle lattice pattern">
        <defs>
          <linearGradient id="plate-sheen" x1="0" y1="0" x2="1" y2="1">
            <stop offset="0" stop-color="var(--plate-light)"/>
            <stop offset="0.5" stop-color="var(--plate-mid)"/>
            <stop offset="1" stop-color="var(--plate-dark)"/>
          </linearGradient>
        </defs>
        <rect width="526" height="536" fill="url(#plate-sheen)"/>
      </svg>
      <div class="nameplate__text">
        <p class="nameplate__name">MAISON</p>
        <p class="nameplate__number">316</p>
      </div>
    </section>
  </main>
</body>
</html>
```